Maison Lumet is a premium domestic placement company and a concept of modern etiquette and a manueri

Maison Lumet is a premium domestic placements agency delivering the most professional caliber of domestic professionals to suit even the most demanding, challenging and refined household tasks.

Based in Dubai, Maisone Lumet the world of Maison Lumet is representing the finest.

We genuinely strive to find the best, recruit the right ones and invest our time and resources for that perfect match.

~ Career Nannies ~
~ Etiquette Governesses ~
~ Royal Protocol Attendees ~
~ Formal Palace Personnel ~
~ Official Butler ~
~ World Class Chefs ~
~ Skilled Housekeepers ~
~ Experienced Babynurses ~
~ Domestic Couples ~
~ Professional Laundresses ~
~ Personal Beautician ~
~ Enthusiastic Chauffeurs ~
~ Gourmet Cooks ~

WEB SITE BRIEF:

Style: clean, classy, refined and screaming luxury - you may see sample i like: www.corvellahouseline.com

Colors: I like black and white with a touch of pink (burned sugar more specifically)

Communicate: The images and the web should communicate class and royalty as i will be working with lots of royal families in the Region.

Images selection: this is very important to me has to be with white, black, and perhaps a touch of pink - just to get along with my logo second line.
1. one image may be a palace
2. may be a housekeeper or a butler
3. something etiquette related! or your
PS. Do not limit to those, its just mine idea and also i don't know why but i prefer images without faces - otherwise looks like endorsement and strong personalization to a face that i dont even know

Note: The pictures i have attached are tentative only

Explanation of my web structure: 1 excel page are the web links 2 are the side links, i want them to be like a sliding tips, that you click to see the next 3 social media i will start with

Standards: You may use my logo (middle icon) as a graphic idea and/or whatever you decide i like consistency - in the colors you use, style and all.

General: Easy to navigate

Thank you all in advance & Enjoy the journey

Marguerite

Target Market(s)

- Royal families and VIP's in Middle East
- Families and families with kids
- Mid and High-end segment singles
- Hotels HR departments
- Companies HR departments
- Celebrities ;)

Industry/Entity Type

It Company

Requirements
Must have
• Standards again of design, i don't like mixed style of photography and drawing and sketches all in one. Think there should be an idea in the backbone
Nice to have
• Clean, i like simple things in life
• Elegant and luxury, reliability and care - that should be the message
• on the MAIN side might have one banner that shows my value added package VIP Maison Lumet consisted of the following:
• - priority served contract
• - draw from the best candidates
• - dedicated consultant
• - FREE couture uniform
• - meeting at your choice
• - FREE training from the Maison Lumet advanced manual
• - FREE cooking book
• - Follow up visit/call
Should not have
• 1. variety of styles as said
• 2. images that are used from others in the same industry and styles
• 3. very big letters - prefer smaller fonts
• 4. illustrations that look cheap

```html
<!DOCTYPE html>
<html lang="en">
<head>
<meta charset="utf-8">
<title>Our Philosophy – Maison Lumet</title>
<link rel="stylesheet" href="https://fonts.googleapis.com/css2?family=Cinzel:wght@400;500;600&family=Gelasio:wght@400&display=swap">
<style>
  :root {
    --ink: #1c1c1c;
    --text: #5a5a5a;
    --muted: #6b6b6b;
    --rule: #d9d9d9;
    --accent: #f0565e;
    --paper: #ffffff;
  }
  * { box-sizing: border-box; margin: 0; padding: 0; }
  html, body {
    width: 1112px; height: 1200px; overflow: hidden;
    background: var(--paper);
  }
  body { position: relative; font-family: "Gelasio", Georgia, serif; color: var(--text); }

  .site-header { position: absolute; left: 154px; top: 0; width: 804px; height: 128px; }
  .brand {
    position: absolute; left: 16px; top: 52px;
    display: flex; align-items: center; gap: 10px;
    font-family: "Cinzel", serif; font-weight: 500; font-size: 19px;
    color: var(--ink); letter-spacing: 0.5px;
  }
  .brand-dot { width: 14px; height: 14px; border: 1px solid var(--ink); border-radius: 50%; }
  .contact-line {
    position: absolute; right: 0; top: 34px; display: flex; align-items: center; gap: 8px;
    font-family: "Cinzel", serif; font-size: 16px; font-weight: 500; color: var(--muted); letter-spacing: 0.6px;
  }
  .contact-line .phone { display: flex; align-items: center; gap: 5px; color: var(--ink); font-family: "Gelasio", Georgia, serif; font-size: 17px; letter-spacing: 0; }
  .main-nav { position: absolute; right: 0; top: 96px; display: flex; gap: 17px; }
  .main-nav a {
    font-family: "Cinzel", serif; font-size: 11.5px; font-weight: 600;
    color: var(--ink); text-decoration: none; letter-spacing: 0.5px;
  }

  .hero {
    position: absolute; left: 154px; top: 128px; width: 804px; height: 351px;
    border-top: 3px solid var(--accent);
    background:
      radial-gradient(ellipse at 52% 38%, #8d8579 0%, transparent 40%),
      linear-gradient(180deg, #6f6a63 0%, #c9c4bb 40%, #a38c6c 68%, #5b4632 100%);
  }

  .content { position: absolute; left: 154px; top: 479px; width: 804px; height: 651px; display: flex; }
  .promise { width: 240px; border-right: 1px solid var(--rule); padding-top: 34px; }
  .promise-title {
    font-family: "Cinzel", serif; font-size: 12.5px; font-weight: 400; letter-spacing: 1.2px;
    color: var(--muted); padding-bottom: 6px; border-bottom: 1px solid var(--rule);
  }
  .promise-item { border-bottom: 1px solid var(--rule); }
  .promise-head {
    display: flex; justify-content: space-between; align-items: center;
    height: 41px; font-family: "Cinzel", serif; font-size: 15.5px; font-weight: 600;
    color: var(--muted); letter-spacing: 0.6px;
  }
  .promise-head .toggle { font-family: "Gelasio", serif; font-size: 14px; margin-right: 14px; color: var(--muted); }
  .promise-item.is-open .promise-head { color: var(--ink); height: 34px; }
  .promise-body { font-size: 12px; line-height: 20.5px; color: var(--ink); padding: 0 18px 10px 0; }

  .philosophy { flex: 1; padding: 24px 0 0 33px; }
  .philosophy h1 {
    font-family: "Cinzel", serif; font-weight: 600; font-size: 27px;
    color: var(--ink); letter-spacing: 0.3px; margin-bottom: 20px;
  }
  .philosophy p { width: 505px; font-size: 12px; line-height: 20.5px; color: var(--text); margin-bottom: 20.5px; }

  .site-footer {
    position: absolute; left: 0; top: 1130px; width: 1112px; height: 70px;
    border-top: 3px solid var(--accent);
  }
  .footer-inner {
    position: absolute; left: 154px; top: 18px; width: 804px;
    display: flex; justify-content: space-between;
    font-family: "Cinzel", serif; font-size: 13px; font-weight: 500; color: var(--ink);
  }
  .footer-links { display: flex; gap: 9px; }
  .footer-links a { color: var(--ink); text-decoration: none; }
  .footer-links .sep { color: var(--muted); }
</style>
</head>
<body>
  <header class="site-header">
    <div class="brand"><span class="brand-dot"></span><span>Maison Lumet</span></div>
    <div class="contact-line">
      <span>Follow up visit/call:</span>
      <span class="phone">
        <svg width="18" height="14" viewBox="0 0 18 14" aria-hidden="true">
          <path d="M1 5 C1 1 17 1 17 5 L17 6 L13 6 L13 4 C11 3 7 3 5 4 L5 6 L1 6 Z" fill="#1c1c1c"/>
          <path d="M4 7 L14 7 L16 13 L2 13 Z" fill="#1c1c1c"/>
          <circle cx="9" cy="10" r="1.8" fill="#fff"/>
        </svg>
        0800 555 019
      </span>
    </div>
    <nav class="main-nav">
      <a href="#">ABOUT</a><a href="#">CLIENTS</a><a href="#">CANDIDATES</a><a href="#">SERVICES</a>
      <a href="#">VIP &amp; ROYAL</a><a href="#">MEDIA</a><a href="#">CONTACT US</a>
    </nav>
  </header>

  <div class="hero" role="img" aria-label="Photograph of a long palace gallery with white columns, gilded painting frames, crystal chandeliers and sunlit parquet floor"></div>

  <main class="content">
    <aside class="promise">
      <h2 class="promise-title">BRAND PROMISE</h2>
      <div class="promise-item is-open">
        <div class="promise-head"><span>RESPECT.</span><span class="toggle">-</span></div>
        <p class="promise-body">At Maison Lumet we care about our fellow human and we do think respecting others is as essential to creating wonderful relationships in life. We respect our Clients and Candidates, our employees and our business collaborators at every level.</p>
      </div>
      <div class="promise-item"><div class="promise-head"><span>SHARING.</span><span class="toggle">+</span></div></div>
      <div class="promise-item"><div class="promise-head"><span>FULFILLMENT.</span><span class="toggle">+</span></div></div>
      <div class="promise-item"><div class="promise-head"><span>HUMAN DIGNITY.</span><span class="toggle">+</span></div></div>
      <div class="promise-item"><div class="promise-head"><span>MANNERS.</span><span class="toggle">+</span></div></div>
      <div class="promise-item"><div class="promise-head"><span>PHILANTHROPY.</span><span class="toggle">+</span></div></div>
    </aside>

    <article class="philosophy">
      <h1>Our Philosophy</h1>
      <p>At Maisone Lumet, we have a special philosophy of living that is imbedded in what we do and our honest efforts of supporting our industry in setting the standards of household staffing a little bit higher. We have bestowed the name of Maison Lumet not only as a concept, but an attitude towards life and work.</p>
      <p>Maisone Lumet is a French phrase; in terms of the actual meaning maison means “house” and lumet means light”. wever the concept also encompasses the customs of a good society and breeding, ability to live life well and with intelligent enjoyment, meeting every situation with poise, good manners, and elegance.</p>
      <p>While the definition of “maison lumet” is rather simple, its meaning is much more romantic and thoughtful. It does not simply mean one knows how to live. Rather, it means one knows how to live well, get the most joy out of life, and live life to the fullest by respecting the inter-cultural differences of life.</p>
      <p>We understood the importance and the responsibility of this when it comes to a region like Middle East especially Dubai as a cosmopolitan place with many cultural and other differences. While these rules and codes remain unique to each culture our professional and social success is based on proper use and understanding of those international behavioral standards. The beauty of the theory of Maison Lumet is something that has to be attained; it does not come without effort. Our Agency would like to promote and support this principle and use as a powerful tool to support peoples life’s. Some of our personnel have been practiced and told how to hold a dose of elegance and class, a forgiven romantic mannerism and etiquette translated into nowadays modern living. If all of us invest in it, the world would be certainly a completely different place.</p>
    </article>
  </main>

  <footer class="site-footer">
    <div class="footer-inner">
      <span>Copyright © 2013 Maison Lumet. All rights reserved.</span>
      <span class="footer-links"><a href="#">Journal</a><span class="sep">|</span><a href="#">News</a><span class="sep">|</span><a href="#">Contact Us</a></span>
    </div>
  </footer>
</body>
</html>
```